Spice Mix Label Bottle Branding - Health and Weight Loss Mixes

The company is called ZestoLane Spice Mix's. We've created 5 spice mixes using ingredients that promote health and weight loss. We already have a logo but now we need labels for our bottles. We would like to see designs that have the feel of health supplements (see attached examples)

We would like a different colour featured with each of our flavours.

Our flavours are:
-Golden Chai (Yellow)
-Mild Curry (Orange)
-Coffee Rub (brown)
-Garlic Oregano (Green)
-Taco (Blue)

Thank you!

Target Market(s)

Ages 22-35. Men and Female. Trendy, Hipster.

Industry/Entity Type

Food Production

Font styles to use
Sans Serif

Colors
f37122
0655a3
0692cd
9bcb3c
fbee3f

Requirements
Must have
• A different featured colour for each flavour.
• The ZestoLane Spices Logo (attached)
• The slogan: "Weight Loss Ingredients"
• -Golden Chai (Yellow)
• -Mild Curry (Orange)
• -Coffee Rub (brown)
• -Garlic Oregano (Green)
• -Taco (Blue)
• Text Files attached.
Nice to have
• A black label with a featured colour for each of the spice mice flavours.
• 'No Salt added'

```html
<!DOCTYPE html>
<html lang="en">
<head>
<meta charset="utf-8">
<title>ZestoLane Spices – Garlic Oregano Label</title>
<link rel="stylesheet" href="https://fonts.googleapis.com/css2?family=Poppins:wght@700&family=Oswald:wght@500&display=swap">
<style>
  :root {
    --page: #f3efe6;
    --label-black: #000000;
    --flavour-green: #9bcb3c;
    --white: #ffffff;
    --ink: #111111;
  }
  html, body {
    margin: 0;
    padding: 0;
    width: 1200px;
    height: 1200px;
    overflow: hidden;
    background: var(--page);
  }
  .canvas {
    position: relative;
    width: 1200px;
    height: 1200px;
  }
  .label {
    position: absolute;
    left: 300px;
    top: 100px;
    width: 600px;
    height: 1000px;
    background: var(--label-black);
    overflow: hidden;
  }
  .label-art {
    position: absolute;
    inset: 0;
    width: 600px;
    height: 1000px;
  }
  .brand {
    position: absolute;
    top: 160px;
    left: 0;
    width: 600px;
    display: flex;
    align-items: center;
    justify-content: center;
    gap: 14px;
  }
  .brand-mark {
    width: 26px;
    height: 26px;
    background: var(--white);
  }
  .brand-name {
    font-family: "Poppins", sans-serif;
    font-weight: 700;
    font-size: 40px;
    color: var(--white);
    letter-spacing: 0.5px;
  }
  .flavour-name {
    position: absolute;
    top: 392px;
    left: 0;
    width: 600px;
    margin: 0;
    text-align: center;
    font-family: "Poppins", sans-serif;
    font-weight: 700;
    font-size: 66px;
    line-height: 1;
    color: var(--ink);
    letter-spacing: -1px;
  }
  .slogan {
    font-family: "Oswald", sans-serif;
    font-weight: 500;
    font-size: 44px;
    fill: var(--white);
  }
  .volume {
    position: absolute;
    right: 14px;
    bottom: 22px;
    font-family: "Oswald", sans-serif;
    font-weight: 500;
    font-size: 18px;
    color: var(--white);
  }
</style>
</head>
<body>
<div class="canvas">
  <div class="label">
    <svg class="label-art" viewBox="0 0 600 1000" xmlns="http://www.w3.org/2000/svg">
      <defs>
        <linearGradient id="top-glow" x1="0" y1="0" x2="0" y2="1">
          <stop offset="0" stop-color="#000000"/>
          <stop offset="0.45" stop-color="#3d5a10"/>
          <stop offset="1" stop-color="#9bcb3c"/>
        </linearGradient>
        <linearGradient id="band" x1="0" y1="0" x2="1" y2="0">
          <stop offset="0" stop-color="#8fc02f"/>
          <stop offset="0.5" stop-color="#a8d447"/>
          <stop offset="1" stop-color="#7fae24"/>
        </linearGradient>
        <radialGradient id="bubble-glow" cx="0.5" cy="0.35" r="0.7">
          <stop offset="0" stop-color="#4c6e14"/>
          <stop offset="1" stop-color="#000000"/>
        </radialGradient>
      </defs>

      <rect class="texture-field" x="0" y="0" width="600" height="360" fill="url(#top-glow)"
            role="img" aria-label="Green halftone dot texture fading into black"/>

      <path class="slogan-band" d="M0 330 H600 V690 C470 745 300 780 160 780 C90 780 40 775 0 768 Z" fill="url(#band)"/>

      <path class="bubble-field" d="M0 768 C40 775 90 780 160 780 C300 780 470 745 600 690 V1000 H0 Z"
            fill="url(#bubble-glow)" role="img" aria-label="Scattered lime green bubble pattern on black"/>

      <path class="name-cloud" fill="#ffffff"
            d="M60 336 C50 318 100 308 140 322 C180 306 230 330 280 318 C330 306 380 328 420 316
               C460 304 510 322 540 316 C575 308 592 334 570 360
               C600 385 598 430 578 450 C600 480 590 520 550 528
               C515 546 465 526 420 536 C370 548 320 530 270 538
               C220 548 170 530 130 538 C85 548 45 530 52 505
               C15 488 14 445 40 430 C16 405 28 350 60 336 Z"/>

      <path id="slogan-arc" d="M55 610 Q300 680 545 595" fill="none"/>
      <text class="slogan" text-anchor="middle">
        <textPath href="#slogan-arc" startOffset="50%">Weight Loss Ingredients</textPath>
      </text>
    </svg>

    <div class="brand">
      <span class="brand-mark"></span>
      <span class="brand-name">ZestoLane Spices</span>
    </div>

    <h1 class="flavour-name">Garlic Oregano</h1>

    <span class="volume">15ML</span>
  </div>
</div>
</body>
</html>
```